Business card design for a world class martial arts and group fitness facility

We need a professional and eye catching design for a business card. The card will be used in networking as well as marketing.
We are a martial arts facility offering Taekwondo, Brazilian Jiu Jitsu, and group fitness. All of our programs are geared for kids and adults.
Our Taekwondo program is lead by a Hall of Fame instructor who was Instructor of the Year in 2015.
Our Brazilian Jiu Jitsu program is lead by a wold class instructor who is also a part of the renown Brazilian KVO team.
We offer 3 focused group fitness programs: Ring striking, Pulse Fitness, and The Meadow which are all lead by certified instructors in a small group setting.
Our facility is state of the art and has been recognized as such in nationally published magazines.
Our business is named The Lantern which is the linear logo that is attached. This is the main logo. I also attached a circular logo we have used in some marketing material. Our Jiu Jitsu program is the KVO team logo. The Taekwondo program is the TORVEX Prime. It would be nice to somehow incorporate all 3 logos, but The Lantern is most important.
Industry/Entity Type
Martial Art
Contact Information for Business Card
We would like to use all 3 logos if possible but The Lantern is the most important. We would like to have a place for a staff member's name while keeping the focus on the programs we offer.
Look and feel
Each slider illustrates characteristics of the customer's brand and the style your logo design should communicate.

```html
<!DOCTYPE html>
<html lang="en">
<head>
<meta charset="utf-8">
<title>The Lantern – Business Card</title>
<link rel="stylesheet" href="https://fonts.googleapis.com/css2?family=Open+Sans:wght@300;400&display=swap">
<style>
  :root {
    --page-bg: #dcd8d3;
    --card-dark: #1f1f21;
    --card-mid: #3b3b3e;
    --text-light: #d8d8d8;
    --text-soft: #cfcfcf;
    --silver-light: #f2f2f2;
    --silver-mid: #c4c4c4;
    --silver-dark: #8f8f8f;
    --ink: #1c1c1c;
    --gi-light: #bdbdbd;
    --gi-dark: #8a8a8a;
  }
  html, body {
    margin: 0;
    padding: 0;
    width: 1200px;
    height: 970px;
    overflow: hidden;
    background: var(--page-bg);
    font-family: "Open Sans", Arial, sans-serif;
  }
  .business-card {
    position: absolute;
    left: 100px;
    top: 207px;
    width: 1000px;
    height: 556px;
    overflow: hidden;
    background: linear-gradient(160deg, var(--card-mid) 0%, var(--card-dark) 70%);
    box-shadow: 0 10px 30px rgba(0,0,0,0.25);
  }
  .offering-title {
    position: absolute;
    left: 60px;
    top: 84px;
    margin: 0;
    font-weight: 300;
    font-size: 68px;
    line-height: 1;
    color: var(--text-light);
    z-index: 2;
  }
  .program-list {
    position: absolute;
    left: 100px;
    width: 267px;
    top: 196px;
    margin: 0;
    padding: 0;
    list-style: none;
    text-align: right;
    z-index: 2;
  }
  .program-list li {
    font-weight: 400;
    font-size: 21px;
    line-height: 36px;
    color: var(--text-soft);
    white-space: nowrap;
  }
  .program-list .tick {
    width: 22px;
    height: 20px;
    margin-left: 9px;
    vertical-align: -2px;
  }
  .uniform-illustration {
    position: absolute;
    left: 0;
    top: 297px;
    width: 250px;
    height: 259px;
    background: linear-gradient(180deg, var(--gi-light) 0%, var(--gi-dark) 100%);
    border-radius: 40px 60px 0 0;
    opacity: 0.75;
    z-index: 1;
  }
  .brand-seal {
    position: absolute;
    left: 416px;
    top: -7px;
    width: 570px;
    height: 570px;
    border-radius: 50%;
    background: radial-gradient(circle at 40% 35%, var(--silver-light) 0%, var(--silver-mid) 55%, var(--silver-dark) 100%);
    display: flex;
    align-items: center;
    justify-content: center;
    z-index: 1;
  }
  .brand-name {
    margin: 0;
    font-weight: 400;
    font-size: 64px;
    color: var(--ink);
    text-transform: uppercase;
    letter-spacing: 2px;
    white-space: nowrap;
  }
</style>
</head>
<body>
  <div class="business-card">
    <h2 class="offering-title">offering</h2>
    <ul class="program-list">
      <li>taekwondo<svg class="tick" viewBox="0 0 22 20"><polyline points="2,11 8,17 20,3" fill="none" stroke="#cfcfcf" stroke-width="2.5"/></svg></li>
      <li>brazilian Jiu Jitsu<svg class="tick" viewBox="0 0 22 20"><polyline points="2,11 8,17 20,3" fill="none" stroke="#cfcfcf" stroke-width="2.5"/></svg></li>
      <li>group fitness<svg class="tick" viewBox="0 0 22 20"><polyline points="2,11 8,17 20,3" fill="none" stroke="#cfcfcf" stroke-width="2.5"/></svg></li>
    </ul>
    <div class="uniform-illustration" role="img" aria-label="Illustration of a martial arts uniform jacket"></div>
    <div class="brand-seal">
      <p class="brand-name">The Lantern</p>
    </div>
  </div>
</body>
</html>
```